Willowmere Equine Sanctuary Flyer Urgent

Willowmere Equine Sanctuary

Rescue • Rehabilitation • Sanctuary

Willowmere Equine Sanctuary provides a safe and ethical refuge for horses, ponies and donkeys who have nowhere else to go. Some arrive needing rehabilitation and careful retraining, while others find permanent sanctuary here due to age, injury or behavioural needs.

Our mission is simple: to improve the physical and psychological wellbeing of every animal in our care.

At Willowmere we focus on:
• Rescue and rehabilitation of horses in need
• Lifetime sanctuary for those who cannot be rehomed
• Education and advocacy for responsible horse care
• Equine rehabilitation services to help horses recover and thrive

Sponsor a Horse

One of the most meaningful ways to support our work is by sponsoring one of our residents. Each horse, pony or donkey only has one sponsor!

Your sponsorship helps provide:
• Hay and feed
• Veterinary care
• Hoof trimming and routine health care
• Rugs, shelter and daily care

Many of our horses will live out their lives here, and sponsorship ensures they are safe, well fed and cared for every single day.

Sponsorship starts from $15 - $25 per week / $60 -$100 per month.

How You Can Help

• Sponsor a horse
• Make a donation
• Share our work with others

Your support helps us continue to say yes to horses who need a second chance.

📍 Willowmere Park, Victoria
📧 clara@willowmerepark-example.org

📞 0400 519 627

Font styles to use
Serif
Sans Serif

Colors
F0912C
F2A743
F7CA91
FBE8D2
FDF5EE
EE7325
F08F49
F5BC92
FAE3D3
FDF4ED

Requirements
Should not have
• Photos not provided by Willowmere

```html
<!DOCTYPE html>
<html lang="en">
<head>
<meta charset="utf-8">
<title>Willowmere Equine Sanctuary – Flyer</title>
<link href="https://fonts.googleapis.com/css2?family=Cinzel:wght@600;700&family=Poppins:wght@400;500;600&display=swap" rel="stylesheet">
<style>
  :root {
    --red: #e0503f;
    --orange: #ee7325;
    --orange-mid: #f08b2e;
    --peach: #f5bc92;
    --peach-light: #fde3ce;
    --pink-light: #fbdbd8;
    --cream: #fdf4ed;
    --ink: #1f1a17;
    --white: #ffffff;
    --serif: "Cinzel", "Times New Roman", serif;
    --sans: "Poppins", Arial, sans-serif;
  }
  * { margin: 0; padding: 0; box-sizing: border-box; }
  html, body { width: 856px; height: 1200px; overflow: hidden; background: var(--white); }
  .flyer { position: relative; width: 856px; height: 1200px; background: var(--white); font-family: var(--sans); color: var(--ink); overflow: hidden; }
  .abs { position: absolute; }

  /* Hero */
  .hero-sky { left: 0; top: 0; width: 856px; height: 200px; background: linear-gradient(180deg, #fdf4ed 0%, #fae3d3 45%, #f5bc92 100%); }
  .hero-panel { left: 0; top: 198px; width: 546px; height: 285px; background: linear-gradient(180deg, #e0641f 0%, #c4501a 45%, #9a3b14 100%); }
  .hero-photo { left: 414px; top: 0; width: 442px; height: 458px; background: linear-gradient(160deg, #f5c9a0 0%, #b8663a 35%, #6b3220 70%, #3d1e14 100%); }
  .brand { left: 61px; top: 72px; display: flex; align-items: center; gap: 12px; }
  .brand-name { font-family: var(--serif); font-weight: 600; color: var(--red); font-size: 24px; line-height: 1.15; }
  .brand-mark { width: 60px; height: 106px; background: var(--orange); }
  .headline { left: 57px; top: 218px; font-family: var(--serif); font-weight: 700; color: var(--white); font-size: 41px; line-height: 42px; letter-spacing: 0.3px; text-shadow: 0 2px 6px rgba(80,30,10,.35); }
  .intro { left: 58px; top: 366px; width: 352px; color: var(--white); font-size: 13.2px; line-height: 16.4px; }
  .hero-line { left: 466px; top: 482px; width: 390px; height: 1.5px; background: var(--peach); }

  /* Mission */
  .mission-title { left: 0; top: 496px; width: 856px; text-align: center; font-family: var(--serif); font-weight: 700; font-size: 31px; color: var(--red); }
  .mission-title .accent { color: var(--orange-mid); }
  .mission-text { left: 0; top: 533px; width: 856px; text-align: center; font-size: 13.4px; font-weight: 500; }
  .focus-pill { left: 254px; top: 563px; width: 348px; height: 21px; border-radius: 11px; background: var(--red); color: var(--white); font-family: var(--serif); font-weight: 600; font-size: 14px; text-align: center; line-height: 21px; letter-spacing: .5px; }
  .focus-card { top: 598px; width: 180px; height: 132px; display: flex; flex-direction: column; align-items: center; justify-content: center; gap: 6px; text-align: center; font-size: 13.4px; font-weight: 500; line-height: 17px; padding: 0 20px; }
  .focus-card.pink { background: var(--pink-light); }
  .focus-card.peach { background: var(--peach-light); }
  .focus-icon { width: 30px; height: 30px; border-radius: 6px; background: linear-gradient(135deg, #f4a692, #e0503f); opacity: .55; }

  /* Sponsor */
  .sponsor-title { left: 57px; top: 745px; font-family: var(--serif); font-weight: 700; font-size: 30px; color: var(--red); }
  .sponsor-title .accent { color: var(--orange-mid); }
  .sponsor-text { left: 58px; top: 786px; width: 345px; font-size: 11px; line-height: 14px; }
  .helps-title { left: 56px; top: 840px; font-family: var(--serif); font-weight: 700; font-size: 15px; color: var(--orange-mid); }
  .helps-list { left: 57px; top: 860px; width: 319px; list-style: none; }
  .helps-list li { height: 27px; display: flex; align-items: center; gap: 7px; font-size: 12.6px; border-bottom: 1px solid #c9c3bf; }
  .helps-list li:last-child { border-bottom: none; }
  .tick { width: 11px; height: 11px; flex: none; }
  .sponsor-close { left: 58px; top: 976px; width: 362px; font-size: 11px; line-height: 14px; }

  .starts-title { left: 452px; top: 744px; font-family: var(--serif); font-weight: 700; font-size: 23.5px; color: var(--orange-mid); white-space: nowrap; }
  .price { top: 780px; width: 168px; height: 86px; display: flex; flex-direction: column; align-items: center; justify-content: center; gap: 4px; color: var(--white); }
  .price.red { left: 452px; background: var(--red); }
  .price.orange { left: 627px; background: var(--orange-mid); }
  .price-amount { font-family: var(--serif); font-weight: 700; font-size: 29px; line-height: 32px; }
  .price-unit { background: var(--white); color: var(--ink); border-radius: 11px; width: 114px; height: 22px; text-align: center; line-height: 22px; font-family: var(--serif); font-weight: 600; font-size: 13px; }
  .or-badge { left: 613px; top: 813px; width: 20px; height: 20px; border-radius: 50%; background: var(--white); font-family: var(--serif); font-weight: 700; font-size: 8px; line-height: 20px; text-align: center; }

  .help-title { left: 452px; top: 877px; font-family: var(--serif); font-weight: 700; font-size: 23.5px; color: var(--orange-mid); }
  .help-card { top: 919px; width: 91px; height: 82px; color: var(--white); font-size: 12px; line-height: 15px; text-align: center; padding-top: 26px; z-index: 2; }
  .help-card.red { background: var(--red); }
  .help-card.orange { background: var(--orange-mid); }
  .help-tick { position: absolute; left: 39px; top: -2px; width: 13px; height: 13px; }

  /* Footer */
  .footer { left: 0; top: 1026px; width: 856px; height: 174px; background: linear-gradient(180deg, #a9461b 0%, #7e3214 55%, #b9541f 100%); }
  .photo-frame { left: 57px; top: 1028px; width: 373px; height: 112px; background: var(--white); }
  .photo { top: 1031px; height: 105px; }
  .photo.one { left: 61px; width: 180px; background: linear-gradient(160deg, #a59078 0%, #5b3a26 55%, #3a2a20 100%); }
  .photo.two { left: 246px; width: 180px; background: linear-gradient(150deg, #c9b89a 0%, #8f6a45 45%, #4a3522 100%); }
  .footer-note { left: 455px; top: 1043px; width: 242px; color: var(--white); font-size: 10.4px; font-weight: 600; line-height: 13.5px; }
  .footer-note .accent { color: var(--orange-mid); }
  .contact { left: 455px; width: 250px; color: var(--white); font-size: 10.4px; display: flex; align-items: center; gap: 5px; }
  .contact svg { width: 10px; height: 10px; flex: none; }
  .animals { left: 738px; top: 917px; width: 118px; height: 283px; border-radius: 50px 10px 0 30px; background: linear-gradient(180deg, #e9e4dd 0%, #cfc7bc 60%, #b9aea2 100%); }
</style>
</head>
<body>
<div class="flyer">
  <div class="abs hero-sky"></div>
  <div class="abs hero-panel"></div>
  <div class="abs hero-photo" role="img" aria-label="Photo of two bay horses nuzzling at sunset"></div>
  <div class="abs hero-line"></div>

  <div class="abs brand">
    <div class="brand-name">Willowmere<br>Equine Sanctuary</div>
    <div class="brand-mark"></div>
  </div>

  <h1 class="abs headline">RESCUE<br>REHABILITATION<br>SANCTUARY</h1>
  <p class="abs intro">Willowmere Equine Sanctuary provides a safe and ethical refuge for horses, ponies and donkeys who have nowhere else to go. Some arrive needing rehabilitation and careful retraining, while others find permanent sanctuary here due to age, injury or behavioural needs.</p>

  <h2 class="abs mission-title">OUR MISSION <span class="accent">IS SIMPLE</span></h2>
  <p class="abs mission-text">To improve the physical and psychological wellbeing of every animal in our care.</p>
  <div class="abs focus-pill">AT WILLOWMERE WE FOCUS ON</div>

  <div class="abs focus-card pink" style="left:59px"><div class="focus-icon" role="img" aria-label="Horse head icon"></div>Rescue and rehabilitation of horses in need</div>
  <div class="abs focus-card peach" style="left:247px"><div class="focus-icon" role="img" aria-label="Heart with horse icon"></div>Lifetime sanctuary for those who cannot be rehomed</div>
  <div class="abs focus-card pink" style="left:434px"><div class="focus-icon" role="img" aria-label="Scales icon"></div>Education and for responsible horse care</div>
  <div class="abs focus-card peach" style="left:621px"><div class="focus-icon" role="img" aria-label="Saddled horse icon"></div>Equine rehabilitation services to help horses recover and thrive</div>

  <h2 class="abs sponsor-title">SPONSOR <span class="accent">A HORSE</span></h2>
  <p class="abs sponsor-text">One of the most meaningful ways to support our work is by sponsoring one of our residents. Each horse, pony or donkey only has one sponsor!</p>
  <h3 class="abs helps-title">YOUR SPONSORSHIP HELPS PROVIDE</h3>
  <ul class="abs helps-list">
    <li><svg class="tick" viewBox="0 0 12 12"><circle cx="6" cy="6" r="6" fill="#e0503f"/><path d="M3.3 6.2l1.8 1.8 3.6-3.8" stroke="#fff" stroke-width="1.4" fill="none"/></svg>Hay and feed</li>
    <li><svg class="tick" viewBox="0 0 12 12"><circle cx="6" cy="6" r="6" fill="#e0503f"/><path d="M3.3 6.2l1.8 1.8 3.6-3.8" stroke="#fff" stroke-width="1.4" fill="none"/></svg>Veterinary care</li>
    <li><svg class="tick" viewBox="0 0 12 12"><circle cx="6" cy="6" r="6" fill="#e0503f"/><path d="M3.3 6.2l1.8 1.8 3.6-3.8" stroke="#fff" stroke-width="1.4" fill="none"/></svg>Hoof trimming and routine health care</li>
    <li><svg class="tick" viewBox="0 0 12 12"><circle cx="6" cy="6" r="6" fill="#e0503f"/><path d="M3.3 6.2l1.8 1.8 3.6-3.8" stroke="#fff" stroke-width="1.4" fill="none"/></svg>Rugs, shelter and daily care</li>
  </ul>
  <p class="abs sponsor-close">Many of our horses will live out their lives here, and sponsorship ensures they are safe, well fed and cared for every single day.</p>

  <h2 class="abs starts-title">SPONSORSHIP STARTS FROM</h2>
  <div class="abs price red"><div class="price-amount">$15 - $25</div><div class="price-unit">PER WEEK</div></div>
  <div class="abs price orange"><div class="price-amount">$60 -$100</div><div class="price-unit">PER MONTH</div></div>
  <div class="abs or-badge">OR</div>

  <h2 class="abs help-title">HOW YOU CAN HELP</h2>
  <div class="abs help-card red" style="left:452px"><svg class="help-tick" viewBox="0 0 14 14"><circle cx="7" cy="7" r="6" fill="none" stroke="#fff" stroke-width="1.2"/><path d="M4.2 7.2l2 2 3.8-4" stroke="#fff" stroke-width="1.3" fill="none"/></svg>Sponsor<br>a horse</div>
  <div class="abs help-card orange" style="left:546px"><svg class="help-tick" viewBox="0 0 14 14"><circle cx="7" cy="7" r="6" fill="none" stroke="#fff" stroke-width="1.2"/><path d="M4.2 7.2l2 2 3.8-4" stroke="#fff" stroke-width="1.3" fill="none"/></svg>Make a<br>donation</div>
  <div class="abs help-card red" style="left:639px"><svg class="help-tick" viewBox="0 0 14 14"><circle cx="7" cy="7" r="6" fill="none" stroke="#fff" stroke-width="1.2"/><path d="M4.2 7.2l2 2 3.8-4" stroke="#fff" stroke-width="1.3" fill="none"/></svg>Share our<br>work with<br>others</div>

  <div class="abs footer"></div>
  <div class="abs photo-frame"></div>
  <div class="abs photo one" role="img" aria-label="Photo of a group of miniature ponies in a paddock"></div>
  <div class="abs photo two" role="img" aria-label="Photo of a young deer and a dog greeting each other"></div>

  <p class="abs footer-note">Your support helps us <span class="accent">continue to say yes to horses</span> who need a second chance.</p>
  <div class="abs contact" style="top:1085px"><svg viewBox="0 0 10 10"><circle cx="5" cy="5" r="5" fill="#f08b2e"/><path d="M5 2.2a1.9 1.9 0 0 0-1.9 1.9C3.1 5.6 5 7.8 5 7.8s1.9-2.2 1.9-3.7A1.9 1.9 0 0 0 5 2.2z" fill="#fff"/></svg>Willowmere Park, Victoria</div>
  <div class="abs contact" style="top:1104px"><svg viewBox="0 0 10 10"><circle cx="5" cy="5" r="5" fill="#f08b2e"/><path d="M3.3 2.6l1 .9-.5.8c.4.8.9 1.3 1.7 1.7l.8-.5.9 1-.6.8C5 7.1 2.9 5 3 3.2z" fill="#fff"/></svg>0400 519 627</div>
  <div class="abs contact" style="top:1123px"><svg viewBox="0 0 10 10"><circle cx="5" cy="5" r="5" fill="#f08b2e"/><rect x="2.6" y="3.3" width="4.8" height="3.4" fill="#fff"/><path d="M2.6 3.3L5 5.2l2.4-1.9" stroke="#f08b2e" stroke-width=".7" fill="none"/></svg>clara@willowmerepark-example.org</div>

  <div class="abs animals" role="img" aria-label="Cut-out photo of a white goat and a white stag"></div>
</div>
</body>
</html>
```